Hollis Vane Turner LLC letterhead/envelope/stationary

Design letterhead and envelope based on prior logo design. Design should be conservative and classic for a defense litigation law firm.

Target Market(s)

Businesses, insurance carriers, construction companies, product manufacturers, healthcare providers, employers, municipalities. In short, the target is businesses that may be sued in court and need civil defense attorneys.

Font styles to use
Serif
Sans Serif

Colors
0255a3

Requirements
Must have
• Straightforward design for letterhead and envelopes including digital format for word. Template should be able to be updated for individual attorneys within the firm. Font should be Trajan Pro if possible to match logo (or a similar font). Firm information is Hollis Vane Turner LLC, 4730 Ridgemont Boulevard, Suite 280, Cedar Ridge, Alabama, 35480. (205)555-0193. other fields that should be included are fax line, direct line, cell phone and email address so that we can update template for each attorney. The color for the logo is 003362
Nice to have
• digital template for microsoft outlook
Should not have
• Busy design/too many graphics

```html
<!DOCTYPE html>
<html lang="en">
<head>
<meta charset="utf-8">
<title>Hollis Vane Turner LLC – Stationery</title>
<link href="https://fonts.googleapis.com/css2?family=Lato:wght@400;700&display=swap" rel="stylesheet">
<style>
  :root {
    --navy: #17365d;
    --ink: #1a1a1a;
    --grey-band: #8a8a8a;
    --canvas: #d7d7d7;
    --paper: #ffffff;
  }
  * { margin: 0; padding: 0; box-sizing: border-box; }
  html, body { width: 1200px; height: 1200px; overflow: hidden; }
  body {
    background: var(--canvas);
    font-family: "Lato", Arial, sans-serif;
    color: var(--ink);
    position: relative;
  }

  /* Letterhead */
  .letterhead {
    position: absolute; left: 63px; top: 205px;
    width: 505px; height: 653px;
    background: var(--paper);
  }
  .letterhead__topband {
    position: absolute; left: 0; top: 0; width: 100%; height: 7px;
    background: var(--navy);
  }
  .firm-name {
    font-family: "Lato", Arial, sans-serif;
    font-weight: 700;
    color: var(--navy);
  }
  .letterhead .firm-name {
    position: absolute; left: 43px; top: 30px;
    width: 120px; font-size: 16px; line-height: 18px;
  }
  .attorney {
    position: absolute; right: 141px; top: 42px;
    text-align: right; font-size: 7px; line-height: 12px;
  }
  .attorney__name { color: var(--navy); font-weight: 700; font-size: 8px; }
  .divider {
    position: absolute; width: 1px; background: var(--navy);
  }
  .letterhead .divider { left: 370px; top: 27px; height: 43px; }
  .contact {
    position: absolute; left: 379px; top: 28px;
    font-size: 7px; line-height: 11.6px; color: var(--navy);
  }
  .contact b { font-weight: 700; }

  .letter-body {
    position: absolute; left: 43px; top: 126px; width: 422px;
    font-size: 9.7px; line-height: 17.4px;
    hyphens: auto;
  }
  .letter-body p { margin-bottom: 17.4px; }
  .sign-off { position: absolute; left: 43px; top: 471px; font-size: 9.7px; }
  .signature {
    position: absolute; left: 35px; top: 487px;
    width: 122px; height: 34px;
    background: linear-gradient(90deg, #f2f2f2, #e6e6e6);
  }
  .closing { position: absolute; left: 43px; top: 541px; font-size: 9.7px; }
  .letter-footer {
    position: absolute; left: 43px; top: 621px;
    font-size: 7.4px; color: var(--navy);
  }
  .letterhead__bottomband { position: absolute; left: 0; bottom: 0; width: 505px; height: 18px; }

  /* Envelopes */
  .envelope {
    position: absolute; left: 600px; width: 549px; height: 249px;
    background: var(--paper);
  }
  .envelope--front { top: 261px; }
  .envelope--back { top: 554px; }
  .envelope--front .firm-name {
    position: absolute; left: 18px; top: 20px;
    width: 92px; font-size: 12px; line-height: 14px;
  }
  .envelope--front .divider { left: 114px; top: 17px; height: 36px; }
  .return-address {
    position: absolute; left: 122px; top: 16px;
    font-size: 7.6px; line-height: 10.5px; color: var(--navy);
  }
  .flap { position: absolute; left: 0; top: 0; width: 549px; height: 80px; }
  .flap__name {
    position: absolute; left: 0; top: 29px; width: 549px; text-align: center;
    color: var(--paper); font-size: 17px; letter-spacing: 1px;
  }
</style>
</head>
<body>

  <section class="letterhead">
    <div class="letterhead__topband"></div>
    <div class="firm-name">Hollis Vane Turner LLC</div>

    <div class="attorney">
      <div class="attorney__name">Mara Ellison</div>
      <div>attorney, xxxyyy xxxzzz</div>
    </div>
    <div class="divider"></div>
    <div class="contact">
      <div><b>C:</b> (205)555-0193</div>
      <div><b>T:</b> (205)555-0193</div>
      <div><b>F:</b> (205)555-0193</div>
      <div><b>E:</b> mellison@hvtlaw.com</div>
    </div>

    <div class="letter-body">
      <p>Lorem Ipsum is simply</p>
      <p>&nbsp;dummy text of the printing and typesetting industry. Lorem Ipsum has been the industry's standard dummy text ever since the 1500s, when an unknown printer took a galley of type and scrambled it to make a type specimen book. It has survived not only five centuries, but also the leap into electronic typesetting, remaining essentially unchanged.</p>
      <p>It is a long established fact that a reader will be distracted by the readable content of a page when looking at its layout. The point of using Lorem Ipsum is that it has a more-or-less normal distribution of letters, as opposed to using 'Content here, content here', making it look like readable English. Many desktop publishing packages and web page editors now use Lorem Ipsum as their default model text, and a search for 'lorem ipsum' will uncover many web sites still in their infancy. Various versions have evolved over the years, sometimes by accident, sometimes on purpose (injected humour and the like).</p>
      <p>&nbsp;Contrary to popular belief, Lorem Ipsum is not simply random text. It has roots in a piece of classical Latin literature from 45 BC, making it over 2000 years old. Edwin Harlow, a Latin professor at Ashford Hill College in Virginia, looked up one of the more obscure Latin words, consectetur, from a Lorem Ipsum passage,</p>
    </div>

    <div class="sign-off">Lorem Ipsum</div>
    <div class="signature" role="img" aria-label="Handwritten attorney signature"></div>
    <div class="closing">Lorem Ipsum is a dummy</div>

    <div class="letter-footer">4730 Ridgemont Boulevard, Suite 280, Cedar Ridge, Alabama, 35480</div>

    <svg class="letterhead__bottomband" viewBox="0 0 505 18" aria-hidden="true">
      <polygon points="0,0 373,0 365,18 0,18" fill="#17365d"/>
      <polygon points="380,0 505,0 505,18 372,18" fill="#8a8a8a"/>
    </svg>
  </section>

  <section class="envelope envelope--front">
    <div class="firm-name">Hollis Vane Turner LLC</div>
    <div class="divider"></div>
    <div class="return-address">
      4730 Ridgemont Boulevard,<br>
      Suite 280, Cedar Ridge,<br>
      Alabama, 35480
    </div>
  </section>

  <section class="envelope envelope--back">
    <svg class="flap" viewBox="0 0 549 80" aria-hidden="true">
      <path d="M0,0 L549,0 L528,72 Q526,78 518,78 L32,78 Q24,78 22,72 Z" fill="#17365d"/>
    </svg>
    <div class="firm-name flap__name">Hollis Vane Turner LLC</div>
  </section>

</body>
</html>
```